Email Marketing for HR and Career Consulting Company

I am looking for a email marketing template that will be developed in HTML format. Right now, we need PSD file format.

The content will include:

1. Featured / Poplar Blog post
2. Latest blog post this week
3. Latest jobs this week
4. Connect with us (social media)

This is a bi-weekly template which we will be sending to people who sign up our weekly newsletter. The purpose of the newsletter is to provide career advise and also latest jobs that's available from our company so that we can redirect them to our career page or apply to our latest jobs.
Updates

Project Deadline Extended
Reason: I am extending this deadline as I would like to see more designs. So far, I have only shortlisted one design that is close to what I am looking for. To all designers, please note that your design would have to be practical and easy to navigate. It also must take into consideration that when we develop this into html, it will b responsive.

Target Market(s)

Job seekers - age group 25 - 45

Industry/Entity Type

Consulting

Font styles to use
Other font styles liked:
• Helvetical

Colors
0492cd
e34197
ec1f27
85cae6
33a6d7
85acd3
eda3c7
e667a6
f59195

Requirements
Must have
• 1. Social media icons
• 2. Links - jobs, contact us
• 3. Popular career advice
• 4. Latest career advice
• 5. Featured jobs
• 6. Popular jobs
Nice to have
• I would like to see clean and minimalist design. Please try to avoid black color. Use pastel colors as much as possible. Our website is www.careerpondly.com.sg
Should not have
• Should avoid black and dark colors

```html
<!DOCTYPE html>
<html lang="en">
<head>
<meta charset="utf-8">
<title>Careerpond Newsletter</title>
<link href="https://fonts.googleapis.com/css2?family=Montserrat:wght@400;600;700&family=Open+Sans:wght@400;600;700&display=swap" rel="stylesheet">
<style>
:root{
  --page:#ececec;
  --card:#ffffff;
  --ink:#3d4650;
  --muted:#8a929a;
  --blue:#0492cd;
  --sky:#33a6d7;
  --pale:#e3f3fb;
  --teal:#1fb39a;
  --grey-btn:#7d8185;
  --rule:#85cae6;
  --pink:#e34197;
  --red:#ec1f27;
}
*{box-sizing:border-box;margin:0;padding:0}
html,body{width:1200px;height:2468px;overflow:hidden;background:var(--page);font-family:"Open Sans",Arial,sans-serif;color:var(--ink)}
.preheader{height:72px;line-height:72px;text-align:center;font-size:13px;color:var(--muted)}
.mail{position:absolute;left:226px;top:72px;width:748px;height:2340px;background:var(--card)}
.masthead{height:148px;display:flex;justify-content:space-between;align-items:center;padding:0 30px}
.brand{display:flex;align-items:center;gap:12px}
.brand-dot{width:56px;height:56px;border-radius:50%;background:var(--sky)}
.brand-name{font-family:"Open Sans",Arial,sans-serif;font-weight:600;font-size:26px;color:var(--ink)}
.follow{text-align:right}
.follow-label{font-size:13px;color:var(--blue);margin-bottom:6px}
.social{display:flex;gap:6px;justify-content:flex-end}
.social span{width:28px;height:28px;border-radius:50%;display:block}
.s1{background:#3b5998}.s2{background:#33a6d7}.s3{background:#e34197}.s4{background:#0492cd}
.hero{position:relative;height:428px}
.hero-photo{position:absolute;inset:0;background:linear-gradient(135deg,#6b5a4a 0%,#a58a6e 40%,#d8d2c8 65%,#7a6c5e 100%)}
.hero-shade{position:absolute;inset:0;background:rgba(30,30,30,.35)}
.hero-copy{position:absolute;left:0;right:0;top:140px;text-align:center;color:#fff}
.hero-title{font-family:"Montserrat",Arial,sans-serif;font-weight:700;font-size:50px;letter-spacing:-.5px}
.hero-sub{font-family:"Montserrat",Arial,sans-serif;font-size:32px;margin-top:2px}
.btn{display:inline-block;font-family:"Montserrat",Arial,sans-serif;font-weight:700;font-size:13px;color:#fff;border-radius:20px;padding:10px 26px;letter-spacing:.5px}
.btn-teal{background:var(--teal);margin-top:26px}
.btn-grey{background:var(--grey-btn)}
.section{text-align:center}
.h2{font-family:"Montserrat",Arial,sans-serif;font-weight:700;font-size:32px;color:var(--ink)}
.h2 em{font-style:normal;color:var(--sky)}
.about{padding-top:28px}
.about p{font-size:14px;line-height:22px;color:var(--ink);margin:18px 60px 0}
.rule{height:2px;background:var(--rule);margin:36px 0 0}
.articles{padding-top:26px}
.grid{display:flex;gap:16px;justify-content:center;margin-top:26px;text-align:left}
.tile{width:222px}
.tile-img{height:220px}
.tile h3{font-size:14px;font-weight:700;line-height:19px;margin-top:14px;color:var(--ink)}
.tile .meta{font-size:11px;color:var(--muted);margin-top:6px}
.more{margin-top:26px}
.img-a{background:linear-gradient(160deg,#cfe6f2,#8fb8d6)}
.img-b{background:linear-gradient(160deg,#9fd0d6,#6fb6bd)}
.img-c{background:linear-gradient(160deg,#f59195,#e6667a)}
.img-d{background:linear-gradient(160deg,#e8e4df,#9a8f86)}
.img-e{background:linear-gradient(160deg,#3a6fa0,#85acd3)}
.img-f{background:linear-gradient(160deg,#b49a80,#5d4a3d)}
.jobs{padding-top:26px}
.jobs-panel{background:var(--pale);margin:28px 24px 0;padding:30px 34px;text-align:left;height:304px}
.job-cat{font-family:"Montserrat",Arial,sans-serif;font-weight:700;font-size:14px;color:var(--ink);margin-bottom:14px}
.job{display:flex;justify-content:space-between;align-items:center;margin-bottom:28px}
.job-title{font-size:15px;font-weight:600;color:var(--sky)}
.job-tags{font-size:10px;color:var(--muted);margin-top:6px;letter-spacing:.5px;word-spacing:14px}
.btn-apply{background:var(--blue);padding:8px 28px;font-size:12px}
.all{margin-top:28px}
.footer{text-align:center;margin-top:34px;font-size:12px;color:var(--muted)}
.footer a{color:var(--blue);text-decoration:none;display:block;margin-top:8px}
.footer .social{justify-content:center;margin-top:22px;gap:10px}
.footer .social span{width:34px;height:34px}
</style>
</head>
<body>
<div class="preheader">Email not displaying correctly? View it in your browser</div>
<main class="mail">
  <header class="masthead">
    <div class="brand"><span class="brand-dot"></span><span class="brand-name">Careerpond</span></div>
    <div class="follow">
      <div class="follow-label">Follow us</div>
      <div class="social"><span class="s1"></span><span class="s2"></span><span class="s3"></span><span class="s4"></span></div>
    </div>
  </header>

  <section class="hero">
    <div class="hero-photo" role="img" aria-label="Photo of hands typing on a laptop beside a job application form"></div>
    <div class="hero-shade"></div>
    <div class="hero-copy">
      <div class="hero-title">The Way of Sucess</div>
      <div class="hero-sub">Start From Here</div>
      <span class="btn btn-teal">FIND MORE</span>
    </div>
  </section>

  <section class="section about">
    <h2 class="h2">About Careerpond</h2>
    <p>Since we started in 2011, Careerpond is widely known as a logistics recruitment specialist who understands the dynamics and real needs of this sector. With our partners and recruiting alliances in Singapore, Malaysia and China, we have been helping clients grow and connect talent across the supply chain.</p>
    <div class="rule"></div>
  </section>

  <section class="section articles">
    <h2 class="h2">Popular <em>career</em> advice</h2>
    <div class="grid">
      <article class="tile"><div class="tile-img img-a" role="img" aria-label="Illustration of a contract document with a pen"></div><h3>Contract Jobs: Can They Really Be A Career Option?</h3><div class="meta">Career Tips · July 02, 2016</div></article>
      <article class="tile"><div class="tile-img img-b" role="img" aria-label="Illustration of a speech bubble saying goodbye"></div><h3>10 Things to Expect After You Have Quit Your Job</h3><div class="meta">Career Tips · July 02, 2016</div></article>
      <article class="tile"><div class="tile-img img-c" role="img" aria-label="Illustration of a hand holding a card"></div><h3>Your Five-Year Plan: Ultimate and Easy Ways for Success</h3><div class="meta">Career Tips · July 02, 2016</div></article>
    </div>
    <div class="more"><span class="btn btn-grey">FIND MORE</span></div>
    <div class="rule"></div>
  </section>

  <section class="section articles">
    <h2 class="h2">Latest <em>blog post</em> this week</h2>
    <div class="grid">
      <article class="tile"><div class="tile-img img-d" role="img" aria-label="Photo of a job interview across a table"></div><h3>The Interview Process Part II: Brace Yourself for Questions</h3></article>
      <article class="tile"><div class="tile-img img-e" role="img" aria-label="Illustration of social network icons on a screen"></div><h3>Your Digital Footprint, Part II: Personal SEO</h3></article>
      <article class="tile"><div class="tile-img img-f" role="img" aria-label="Photo of a desk with a laptop and coffee"></div><h3>Cultivating Your References</h3></article>
    </div>
    <div class="more"><span class="btn btn-grey">FIND MORE</span></div>
    <div class="rule"></div>
  </section>

  <section class="section jobs">
    <h2 class="h2">Featured jobs</h2>
    <div class="jobs-panel">
      <div class="job-cat">HUMAN RESOURCE</div>
      <div class="job">
        <div><div class="job-title">Senior / Recruitment Consultant - Executive Search Division</div><div class="job-tags">SINGAPORE HUMAN RESOURCE FULL TIME</div></div>
        <span class="btn btn-apply">APPLY</span>
      </div>
      <div class="job-cat">INFORMATION TECHNOLOGY</div>
      <div class="job">
        <div><div class="job-title">TMS Support Analyst, APAC</div><div class="job-tags">SINGAPORE HUMAN RESOURCE FULL TIME</div></div>
        <span class="btn btn-apply">APPLY</span>
      </div>
    </div>
    <div class="all"><span class="btn btn-grey">VIEW ALL JOBS</span></div>
  </section>

  <footer class="footer">
    Copyright © 2016 www.careerpondly.com.sg. All rights reserved
    <a href="#">unsubscribe from this list</a>
    <div class="social"><span class="s1"></span><span class="s2"></span><span class="s3"></span><span class="s4"></span></div>
  </footer>
</main>
</body>
</html>
```